Business Card with Multiple Logos

We are looking for a simple and elegant card covering all our brand Logos (VELMO, DishWagon, Tilverna, VELMO Express) and showing what all we do (Restaurants, Catering, Import & Distribution, Information Technology). The name of the company is "KORVI Ventures" which we prefrably want as EMBOSS. The information should be easy to read. Incase required, i am open for a foldable card. I am also interested to use recycled paper.
Updates
+ An Overview / Background of the Business & ServicesWe are into Import & Distribution, Restaurants, Catering | Concept Retail Store & IT services. All these services represent their parent company Sharing the common group name e.g. KORVI Logistics, KORVI Supermart, KORVI Hospitality, etc. And the main (Share Holding Company name is KORVI Ventures) For the key management people. I am looking for a concept that "KORVI Ventures" whould be mentioned on the card and inside either we show all the sub division company names, and/or their Brand Logos+ The Target Market / Audience you are trying to reachBusiness Associates+ Design Specifics; any preferences or ideas for Style, Colour, Imagery, etcIt should be classy, but sober at the same time. Although we have Orange as a color theme but I am open to explore something new as well. + Contact information to be included in the cardsBusiness Address (Plaza 47, Ratvinai Soi 38, Opp. R L Bentoria Hotel, Banphraek, Bangkok 10590 Thailand)Contact Details T : +662 735 2917 | F : +662 735 2918 | W : www.korvi.ventures | E : rm@korvi.ventures Added Friday, March 27, 2015
Industry/Entity Type
Business
Contact Information for Business Card
Name : Rohan Malvekar
Designation : Group Director
Address : Plaza 47, Ratvinai Soi 38, Banphraek, Bangkok 10590 Thailand (Landmark : Opp. R L Bentoria Hotel)
Email : rm@korvi.ventures | M : +66897260135 | W : www.korvi.ventures
Contact : O : +662 735 2917 | F : +662 735 2918
Requirements
Must have
- Our Brand Logos (4 in number)

```html
<!DOCTYPE html>
<html lang="en">
<head>
<meta charset="utf-8">
<title>VELMO Express – Business Card</title>
<link href="https://fonts.googleapis.com/css2?family=Exo+2:wght@400;600&display=swap" rel="stylesheet">
<style>
  :root{
    --bg:#e9e7e3;
    --card:#f7f7f7;
    --card-shade:#e4e5e7;
    --navy:#0d4f8b;
    --orange:#ee5a24;
    --ink:#3a3f47;
  }
  *{margin:0;padding:0;box-sizing:border-box}
  html,body{width:1200px;height:903px;overflow:hidden}
  body{background:var(--bg);font-family:"Exo 2",sans-serif;position:relative}
  .card{
    position:absolute;width:540px;height:310px;
    background:linear-gradient(135deg,var(--card) 0%,#ffffff 45%,var(--card-shade) 100%);
    box-shadow:0 8px 24px rgba(0,0,0,.12);
    overflow:hidden;
  }
  .card--back{left:630px;top:296px}
  .card--front{left:30px;top:296px}

  .brand{position:absolute;color:var(--orange);font-weight:600;letter-spacing:.5px;white-space:nowrap}
  .card--back .brand{left:0;right:0;top:118px;text-align:center;font-size:44px;line-height:52px}
  .card--front .brand{left:150px;top:40px;font-size:30px;line-height:36px}

  .group{position:absolute;left:0;right:0;text-align:center;color:var(--navy)}
  .group__name{top:182px;font-size:15px;font-weight:600;letter-spacing:2px}
  .group__brands{top:206px;font-size:12px;color:var(--ink);letter-spacing:.5px}

  .accent-block{position:absolute;left:130px;top:0;width:60px;height:30px;background:var(--navy)}
  .accent-bar{position:absolute;left:280px;top:118px;width:260px;height:28px;background:var(--navy)}

  .address{position:absolute;left:28px;top:112px;width:230px;display:flex;gap:8px;
    font-size:12px;line-height:17px;color:var(--ink)}
  .address svg{flex:none;margin-top:1px}
  .company{position:absolute;left:48px;top:180px;font-size:12px;font-weight:600;
    color:var(--navy);letter-spacing:1px}

  .person{position:absolute;left:292px;top:154px}
  .person__name{font-size:17px;font-weight:600;color:var(--navy);letter-spacing:1px;line-height:21px}
  .person__title{font-size:12px;color:var(--ink);line-height:16px}

  .contacts{position:absolute;left:212px;top:204px;list-style:none;
    font-size:11.5px;color:var(--ink)}
  .contacts li{display:flex;align-items:center;gap:8px;height:18px;white-space:nowrap}
  .contacts svg{flex:none}
</style>
</head>
<body>

<section class="card card--back" aria-label="Card back">
  <div class="brand">VELMO Express</div>
  <p class="group group__name">KORVI VENTURES</p>
  <p class="group group__brands">VELMO · DishWagon · Tilverna · VELMO Express</p>
</section>

<section class="card card--front" aria-label="Card front">
  <div class="accent-block"></div>
  <div class="brand">VELMO Express</div>
  <div class="accent-bar"></div>

  <div class="address">
    <svg width="12" height="16" viewBox="0 0 12 16"><path d="M6 0a6 6 0 0 0-6 6c0 4.5 6 10 6 10s6-5.5 6-10a6 6 0 0 0-6-6zm0 8.5A2.5 2.5 0 1 1 6 3.5a2.5 2.5 0 0 1 0 5z" fill="#0d4f8b"/></svg>
    <p>Plaza 47, Ratvinai Soi 38,<br>Banphraek, Bangkok 10590<br>Thailand</p>
  </div>
  <p class="company">KORVI VENTURES</p>

  <div class="person">
    <p class="person__name">ROHAN MALVEKAR</p>
    <p class="person__title">Group Director</p>
  </div>

  <ul class="contacts">
    <li><svg width="11" height="11" viewBox="0 0 12 12"><path d="M2.5 0.5l2 2.5-1.2 1.4a7 7 0 0 0 4.3 4.3L9 7.5l2.5 2-1 2C5 11.5.5 7 .5 1.5z" fill="#0d4f8b"/></svg>+662 735 2917</li>
    <li><svg width="11" height="11" viewBox="0 0 12 12"><rect x="3" y="0.5" width="6" height="11" rx="1.2" fill="none" stroke="#0d4f8b" stroke-width="1.3"/><circle cx="6" cy="9.6" r=".8" fill="#0d4f8b"/></svg>+66897260135</li>
    <li><svg width="11" height="11" viewBox="0 0 12 12"><rect x="0.5" y="4" width="11" height="7" fill="#0d4f8b"/><rect x="3" y="0.5" width="6" height="4" fill="none" stroke="#0d4f8b"/></svg>+662 735 2918</li>
    <li><svg width="11" height="11" viewBox="0 0 12 12"><rect x="0.5" y="2" width="11" height="8" fill="#0d4f8b"/><path d="M.5 2L6 7l5.5-5" stroke="#fff" fill="none"/></svg>rm@korvi.ventures</li>
    <li><svg width="11" height="11" viewBox="0 0 12 12"><circle cx="6" cy="6" r="5.4" fill="#0d4f8b"/><path d="M.6 6h10.8M6 .6v10.8M6 .6c-3 3-3 7.8 0 10.8M6 .6c3 3 3 7.8 0 10.8" stroke="#fff" stroke-width=".7" fill="none"/></svg>www.korvi.ventures</li>
  </ul>
</section>

</body>
</html>
```